Telecommunications Company needs a business card design

We are looking for a sleek, professional and modern business card design based off our new logo. Will look at both light and dark options. On some designs please provide a small space for a QR code

Target Market(s)

B2B clients in Australia

Contact Information for Business Card

Name, Position, Brisbane (head) office, Phone number, email address, QR code (link to our website brightlinktelco.com.au

Colors
0054AA
0677BA
7BADD7
CADEEF
E8F1F8
0094D4
00A9DD
6FCCEA
C7EBF8
E9F6FB
00AB8E
00BBA5
67D7C9
C6EFE9
E9F9F6

```html
<!DOCTYPE html>
<html lang="en">
<head>
<meta charset="utf-8">
<title>Brightlink Telco – Business Card Back</title>
<link rel="stylesheet" href="https://fonts.googleapis.com/css2?family=Montserrat:wght@400;600&family=Arimo:wght@400&display=swap">
<style>
  :root {
    --card-bg: #ffffff;
    --ink: #111111;
    --brand: #0677BA;
    --brand-accent: #00AB8E;
  }
  html, body {
    margin: 0;
    padding: 0;
    width: 1200px;
    height: 695px;
    overflow: hidden;
    background: var(--card-bg);
  }
  .card {
    position: relative;
    width: 1200px;
    height: 695px;
    background: var(--card-bg);
    color: var(--ink);
  }
  .contact {
    position: absolute;
    top: 66px;
    margin: 0;
    font-family: "Montserrat", sans-serif;
    font-weight: 400;
    font-size: 28px;
    letter-spacing: 1.6px;
    line-height: 1;
  }
  .contact--email { left: 45px; }
  .contact--web { right: 66px; }
  .brand {
    position: absolute;
    left: 0;
    right: 0;
    top: 300px;
    display: flex;
    justify-content: center;
    align-items: center;
    gap: 20px;
  }
  .brand__mark {
    width: 44px;
    height: 44px;
    background: var(--brand-accent);
  }
  .brand__name {
    margin: 0;
    font-family: "Montserrat", sans-serif;
    font-weight: 600;
    font-size: 62px;
    letter-spacing: 1px;
    color: var(--brand);
    line-height: 1;
  }
  .services {
    position: absolute;
    left: 0;
    right: 0;
    top: 563px;
    margin: 0;
    padding: 0;
    list-style: none;
    display: flex;
    justify-content: center;
    font-family: "Arimo", sans-serif;
    font-size: 25px;
    line-height: 1;
    white-space: pre;
  }
</style>
</head>
<body>
  <main class="card">
    <p class="contact contact--email">info@companywebsite.com</p>
    <p class="contact contact--web">www.companywebsite.com</p>

    <div class="brand">
      <span class="brand__mark" aria-hidden="true"></span>
      <h1 class="brand__name">Brightlink Telco</h1>
    </div>

    <ul class="services">
      <li>Service 1 I   Service 2  I   Service 3  I     Service 3    I    Service 4</li>
    </ul>
  </main>
</body>
</html>
```